Banner Ad for website hompage - Design Project

We need 4 banner ads for the homepage of a Rent a Car company based in dubai. We rent a wide range of cars but mainly deal in the affordable cars category. Our website colors are mainly red, white and black and I can send pictures of the website (attached) if you want something to compare possible design ideas with. The banners need to promote different messages and must be appealing to the end user. It must also use pictures of cars that exist in our fleet (Pls note: this is only if you are using cars in the banner ad)

The 4 banner ads needed are as follows:
1) should promote something along the lines of we have 20+ models available and reserve a car now (This banner should also have a reserve now button, not the actual button but it's design. The button will be made and coded by us)
2) should promote something along the lines of we offer personalised service and we look after each and every custoemr individually
3) we provide attractive rates based on daily, weekly, monthly and longer rental periods (should also incorporate a reserve now message)
4) Like us on quorvia and follow us on social media for additional offers and discounts (would like for this to have a like button design implemented in it which will be linked to quorvia.)

Also please not the picture file size is 940pixels by 400pixels

Finally: I also need the psd files for the banners.

```html
<!DOCTYPE html>
<html lang="en">
<head>
<meta charset="utf-8">
<title>Crestline Rent a Car – Home</title>
<link rel="stylesheet" href="https://fonts.googleapis.com/css2?family=Arimo:wght@400;700&family=Gelasio:ital@1&family=Source+Sans+3:wght@400;600;700&display=swap">
<style>
  :root {
    --brand-red: #d42a10;
    --brand-red-dark: #b81f08;
    --band-red: #cf2a0e;
    --header-bg: #f7f7f7;
    --page-bg: #f3f3f3;
    --nav-text: #4a4a4a;
    --nav-active: #c0301a;
    --body-text: #5c5c5c;
    --heading-text: #555555;
    --strong-text: #444444;
    --rule: #dddddd;
    --white: #ffffff;
    --button-dark: #2a1a18;
  }
  * { box-sizing: border-box; margin: 0; padding: 0; }
  html, body { width: 1200px; height: 870px; overflow: hidden; }
  body { position: relative; background: var(--page-bg); font-family: "Arimo", Arial, sans-serif; }

  .top-band { position: absolute; left: 0; top: 0; width: 1200px; height: 29px; background: var(--band-red); }

  .site-header { position: absolute; left: 0; top: 29px; width: 1200px; height: 116px;
    background: linear-gradient(#ffffff, var(--header-bg)); }
  .brand { position: absolute; left: 152px; top: 34px; display: flex; align-items: center; gap: 10px;
    font-family: "Source Sans 3", sans-serif; font-weight: 700; font-size: 30px; color: var(--brand-red); }
  .brand-dot { width: 16px; height: 16px; border-radius: 50%; background: var(--brand-red); }

  .main-nav { position: absolute; top: 59px; left: 0; width: 1200px; font-family: "Arimo", Arial, sans-serif;
    font-size: 11.5px; font-weight: 700; letter-spacing: 0.2px; color: var(--nav-text); }
  .main-nav a { position: absolute; color: inherit; text-decoration: none; white-space: nowrap; }
  .main-nav a.is-active { color: var(--nav-active); }

  .hero { position: absolute; left: 0; top: 145px; width: 1200px; height: 374px; background: var(--band-red); }
  .hero-banner { position: absolute; left: 147px; top: 0; width: 881px; height: 374px; overflow: hidden;
    background: linear-gradient(100deg, #d8350f 0%, #dd3d14 30%, #c82a0c 55%, #b3240a 100%); }
  .hero-photo { position: absolute; left: 300px; top: 0; width: 581px; height: 374px;
    background:
      radial-gradient(ellipse 60% 30% at 70% 45%, rgba(90,150,210,0.85), transparent 70%),
      radial-gradient(ellipse 45% 25% at 85% 22%, rgba(220,30,40,0.9), transparent 70%),
      radial-gradient(ellipse 70% 35% at 60% 82%, rgba(240,200,30,0.95), transparent 70%),
      linear-gradient(100deg, rgba(200,40,12,1) 0%, rgba(160,30,20,0.6) 40%, rgba(70,40,50,0.7) 100%); }
  .hero-sheen { position: absolute; inset: 0; }
  .hero-copy { position: absolute; left: 58px; top: 50px; color: var(--white); font-family: "Source Sans 3", sans-serif; }
  .hero-title { font-size: 31px; font-weight: 700; line-height: 1; }
  .hero-title .hero-number { font-size: 50px; }
  .hero-sub { font-size: 23px; font-weight: 400; line-height: 30px; margin-top: 6px; }
  .reserve-button { position: absolute; left: 58px; top: 280px; width: 177px; height: 34px; border-radius: 6px;
    background: linear-gradient(#4a3431, var(--button-dark) 55%, #150c0b);
    box-shadow: 0 2px 3px rgba(0,0,0,0.45), inset 0 1px 0 rgba(255,255,255,0.25);
    color: var(--white); font-family: "Source Sans 3", sans-serif; font-weight: 700; font-size: 15px;
    display: flex; align-items: center; justify-content: center; }

  .intro { position: absolute; left: 152px; top: 552px; width: 582px; }
  .intro-heading { font-family: "Arimo", Arial, sans-serif; font-size: 16.5px; font-weight: 400; color: var(--heading-text); letter-spacing: 0.2px; }
  .intro-heading strong { font-weight: 700; }
  .intro-text { margin-top: 11px; font-size: 12.6px; line-height: 18.6px; color: var(--body-text); }
  .intro-text strong { color: var(--strong-text); }

  .ceo-quote { position: absolute; left: 761px; top: 588px; width: 275px; }
  .quote-mark { position: absolute; left: 0; top: -4px; font-family: "Gelasio", Georgia, serif; font-style: italic; font-size: 44px; line-height: 1; color: #888; }
  .quote-text { padding-left: 31px; font-family: "Gelasio", Georgia, serif; font-style: italic; font-size: 15.2px; line-height: 22.3px; color: #6a6a6a; }
  .quote-author { padding-left: 31px; margin-top: 8px; font-size: 12.6px; font-weight: 700; color: #444; }

  .section-rule { position: absolute; left: 152px; top: 731px; width: 880px; height: 1px; background: var(--rule); }

  .feature-tile { position: absolute; top: 767px; height: 103px; }
  .tile-about { left: 152px; width: 281px; background: radial-gradient(circle at 40% 60%, #9a9a9a, #2b2b2b 55%, #0c0c0c); }
  .tile-services { left: 452px; width: 280px; background: linear-gradient(110deg, #e8501c, #f07a22 55%, #f6a332); }
  .tile-contact { left: 751px; width: 281px; background: linear-gradient(180deg, #f4f4f4, #e6e6e6); }
</style>
</head>
<body>
  <div class="top-band"></div>

  <header class="site-header">
    <div class="brand"><span class="brand-dot"></span>Crestline Rent a Car</div>
    <nav class="main-nav">
      <a class="is-active" style="left:493px">HOME</a>
      <a style="left:556px">ABOUT US</a>
      <a style="left:642px">SERVICES &amp; BENEFITS</a>
      <a style="left:790px">BLOG</a>
      <a style="left:851px">CONTACT US</a>
      <a style="left:951px">RESOURCES</a>
    </nav>
  </header>

  <section class="hero">
    <div class="hero-banner">
      <div class="hero-photo" role="img" aria-label="Photo of a row of colourful parked cars in red, blue and yellow"></div>
      <svg class="hero-sheen" width="881" height="374" viewBox="0 0 881 374" aria-hidden="true">
        <polygon points="0,0 190,0 320,374 0,374" fill="#e3431a" opacity="0.35"/>
        <polygon points="190,0 330,0 460,374 320,374" fill="#ffffff" opacity="0.05"/>
      </svg>
      <div class="hero-copy">
        <p class="hero-title">We have <span class="hero-number">20+</span></p>
        <p class="hero-sub">models available and<br>reserve a car now</p>
      </div>
      <div class="reserve-button">Reserve Now</div>
    </div>
  </section>

  <section class="intro">
    <h2 class="intro-heading">Rent a car with us, <strong>an adventure</strong> awaits you</h2>
    <p class="intro-text">Whether you are a current resident of the wonderful city of Dubai, a traveler stopping by on his/her way or a tourist waiting to pounce on the amazing adventure that is Dubai; Crestline Rent a Car is there for you. We provide cars suited for any occasion (whether it be exploring and conquering the wonders of Dubai, taking a relaxing drive along with your family, travelling from one point to another or even shopping) combined with exceptional customer service, allowing you to <strong>experience a new world on wheels.</strong></p>
  </section>

  <blockquote class="ceo-quote">
    <span class="quote-mark">&ldquo;</span>
    <p class="quote-text">At Crestline we strive to provide an exceptional service while at the same time providing a personal experience that is individual to each and every customer.</p>
    <p class="quote-author">— Omar Halvesen (CEO)</p>
  </blockquote>

  <div class="section-rule"></div>

  <div class="feature-tile tile-about" role="img" aria-label="Photo of a pinned note asking about us, lit by a desk lamp"></div>
  <div class="feature-tile tile-services" role="img" aria-label="Orange graphic introducing our services"></div>
  <div class="feature-tile tile-contact" role="img" aria-label="Photo of a pen writing a contact note on paper"></div>
</body>
</html>
```